business card design and letterhead for a building inspection company. We have a pre-purchase building and pest inspection ( i inspect house before people purchase it)
Updates

Tilda has been so so responsive and good, i highly recommend her

Industry/Entity Type

Building

Contact Information for Business Card

audience, solicitor, real estate agent, mortgage brokerthe rest of the info will be in the attachement business card

```html
<!DOCTYPE html>
<html lang="en">
<head>
<meta charset="utf-8">
<title>SURELOOK Property Inspections – Business Card</title>
<link href="https://fonts.googleapis.com/css2?family=Open+Sans:wght@400;600;700&display=swap" rel="stylesheet">
<style>
  :root {
    --backdrop: #e4e6e8;
    --card-white: #ffffff;
    --card-grey: #eceeef;
    --brand-blue: #1877c0;
    --ink-black: #0d0d0d;
    --text-white: #ffffff;
  }
  html, body {
    margin: 0;
    width: 1200px;
    height: 900px;
    overflow: hidden;
    background: var(--backdrop);
    font-family: "Open Sans", Arial, sans-serif;
  }
  .business-card {
    position: absolute;
    left: 150px;
    top: 195px;
    width: 900px;
    height: 510px;
    border-radius: 48px;
    overflow: hidden;
    background: radial-gradient(ellipse at 40% 30%, var(--card-white) 0%, var(--card-grey) 100%);
    box-shadow: 0 10px 30px rgba(0,0,0,0.18);
  }
  .card-shapes {
    position: absolute;
    inset: 0;
  }
  .brand-block {
    position: absolute;
    left: 300px;
    top: 110px;
    display: flex;
    align-items: center;
    gap: 14px;
  }
  .brand-square {
    width: 46px;
    height: 46px;
    border: 5px solid var(--brand-blue);
    box-sizing: border-box;
  }
  .brand-text { line-height: 1; }
  .brand-name {
    font-size: 50px;
    font-weight: 700;
    color: var(--brand-blue);
    letter-spacing: 1px;
  }
  .brand-sub {
    font-size: 15px;
    font-weight: 600;
    color: var(--ink-black);
    letter-spacing: 1.5px;
    margin-top: 4px;
  }
  .brand-tagline {
    font-size: 13px;
    color: var(--brand-blue);
    letter-spacing: 1.2px;
    margin-top: 3px;
  }
  .holder {
    position: absolute;
    right: 36px;
    top: 262px;
    text-align: right;
    color: var(--text-white);
  }
  .holder-name { font-size: 26px; font-weight: 700; line-height: 1.2; }
  .holder-role { font-size: 21px; margin-top: 2px; line-height: 1.2; }
  .contact-list {
    position: absolute;
    left: 60px;
    top: 347px;
    margin: 0;
    padding: 0;
    list-style: none;
    color: var(--text-white);
    font-size: 15px;
    line-height: 1.35;
  }
  .contact-list li {
    display: flex;
    align-items: flex-start;
    gap: 10px;
  }
  .contact-list .icon {
    flex: none;
    width: 15px;
    height: 15px;
    margin-top: 3px;
  }
  .contact-list .spaced { margin-top: 8px; }
</style>
</head>
<body>
  <div class="business-card">
    <svg class="card-shapes" viewBox="0 0 900 510" width="900" height="510" aria-hidden="true">
      <path fill="var(--brand-blue)" d="M0 340 C 250 322, 470 322, 580 308 C 720 280, 820 180, 900 100 L900 510 L0 510 Z"/>
      <path fill="var(--ink-black)" d="M8 330 C 300 292, 500 292, 610 250 C 680 220, 725 150, 740 85 C 738 150, 700 220, 625 262 C 500 308, 300 306, 8 330 Z"/>
      <path fill="var(--ink-black)" d="M540 298 C 660 258, 745 175, 780 60 C 788 150, 725 240, 580 302 Z"/>
    </svg>

    <div class="brand-block">
      <div class="brand-square"></div>
      <div class="brand-text">
        <div class="brand-name">SURELOOK</div>
        <div class="brand-sub">PROPERTY INSPECTIONS</div>
        <div class="brand-tagline">The building and pest expert</div>
      </div>
    </div>

    <div class="holder">
      <div class="holder-name">Sarah Tilda</div>
      <div class="holder-role">Owner / C.E.O</div>
    </div>

    <ul class="contact-list">
      <li>
        <svg class="icon" viewBox="0 0 16 16"><circle cx="8" cy="8" r="8" fill="#fff"/><path d="M8 3.5a3 3 0 0 0-3 3c0 2.2 3 6 3 6s3-3.8 3-6a3 3 0 0 0-3-3z" fill="var(--brand-blue)"/></svg>
        <span>Suite # 118, Elm Court,<br>NY 10452</span>
      </li>
      <li class="spaced">
        <svg class="icon" viewBox="0 0 16 16"><circle cx="8" cy="8" r="8" fill="#fff"/><path d="M5 4l2 2-1 1.2c.6 1.2 1.6 2.2 2.8 2.8L10 9l2 2-1.3 1.3C7.5 12 4 8.5 3.7 5.3z" fill="var(--brand-blue)"/></svg>
        <span>555-201-4408</span>
      </li>
      <li>
        <svg class="icon" viewBox="0 0 16 16"><circle cx="8" cy="8" r="8" fill="#fff"/><rect x="5.5" y="3.5" width="5" height="9" rx="1" fill="var(--brand-blue)"/></svg>
        <span>555-318-7721</span>
      </li>
      <li>
        <svg class="icon" viewBox="0 0 16 16"><circle cx="8" cy="8" r="8" fill="#fff"/><rect x="5" y="4" width="6" height="8" rx="1" fill="none" stroke="var(--brand-blue)" stroke-width="1.5"/></svg>
        <span>555-640-2953</span>
      </li>
      <li>
        <svg class="icon" viewBox="0 0 16 16"><circle cx="8" cy="8" r="8" fill="#fff"/><rect x="4" y="5" width="8" height="6" fill="var(--brand-blue)"/><path d="M4 5l4 3.5L12 5" fill="none" stroke="#fff" stroke-width="1"/></svg>
        <span>hello@surelookinspect.com</span>
      </li>
      <li>
        <svg class="icon" viewBox="0 0 16 16"><circle cx="8" cy="8" r="8" fill="#fff"/><circle cx="8" cy="8" r="4.5" fill="none" stroke="var(--brand-blue)" stroke-width="1.3"/><path d="M3.5 8h9M8 3.5c-2 2.5-2 6.5 0 9M8 3.5c2 2.5 2 6.5 0 9" fill="none" stroke="var(--brand-blue)" stroke-width="1"/></svg>
        <span>www.surelookinspect.com</span>
      </li>
    </ul>
  </div>
</body>
</html>
```